Business Card for Technology Startup

Design a 2-sided business card using the logo provided. We are a digital healthcare platform that provides a mobile app and web UI that helps caregivers, families, and doctors share information and provide better patient outcomes. We use AI and machine learning to help guide patients through their day-to-day life. The final design should communicate stability, peace, comfort, but also align with the image of an AI-driven technology startup.

I'd like the deliverable to by a Photoshop PSD file (with layers) that I can work with in pixlr.com. Should contain the following editable layers:
Name (ex. Karl Whitby)
Title (ex. Founder / CEO)
Email (ex. info@morventary.ai)
Phone (ex. (999) 482-7160)
Website (ex. https://morventary.ai)

```html
<!DOCTYPE html>
<html lang="en">
<head>
<meta charset="utf-8">
<title>Morventary Business Card</title>
<link rel="stylesheet" href="https://fonts.googleapis.com/css2?family=Montserrat:wght@400;500;700;800&display=swap">
<style>
  :root {
    --canvas-bg: #5f5f5f;
    --card-bg: #232323;
    --card-emboss: #2d2d2d;
    --text-light: #ffffff;
    --accent-blue: #29aee6;
    --card-radius: 22px;
  }
  * { margin: 0; padding: 0; box-sizing: border-box; }
  html, body {
    width: 1200px;
    height: 875px;
    overflow: hidden;
    background: var(--canvas-bg);
    font-family: "Montserrat", sans-serif;
  }
  .sheet {
    width: 1200px;
    height: 875px;
    display: flex;
    flex-direction: column;
    align-items: center;
    justify-content: center;
    gap: 25px;
  }
  .card {
    position: relative;
    width: 700px;
    height: 400px;
    background: var(--card-bg);
    border-radius: var(--card-radius);
    box-shadow: 0 6px 18px rgba(0,0,0,0.35);
  }

  /* Back side: embossed wordmark */
  .card-back {
    display: flex;
    align-items: center;
    justify-content: center;
    gap: 22px;
  }
  .emboss-dot {
    width: 38px;
    height: 38px;
    border-radius: 50%;
    background: var(--card-emboss);
  }
  .emboss-name {
    font-weight: 800;
    font-size: 92px;
    letter-spacing: 1px;
    color: var(--card-emboss);
  }

  /* Front side: logo + contact block */
  .card-front {
    display: flex;
    align-items: center;
    padding-left: 95px;
  }
  .brand {
    display: flex;
    align-items: center;
    gap: 14px;
  }
  .brand-dot {
    width: 20px;
    height: 20px;
    border-radius: 50%;
    background: var(--accent-blue);
  }
  .brand-name {
    font-weight: 800;
    font-size: 48px;
    color: var(--text-light);
  }
  .divider {
    width: 1px;
    height: 175px;
    background: var(--accent-blue);
    margin: 0 34px 0 32px;
  }
  .contact-block {
    display: flex;
    flex-direction: column;
  }
  .person-name {
    font-weight: 700;
    font-size: 26px;
    letter-spacing: 0.5px;
    text-transform: uppercase;
    color: var(--text-light);
    line-height: 1.1;
  }
  .person-title {
    font-weight: 500;
    font-size: 20px;
    color: var(--accent-blue);
    margin-bottom: 16px;
  }
  .contact-list { list-style: none; }
  .contact-item {
    display: flex;
    align-items: center;
    gap: 10px;
    font-weight: 400;
    font-size: 17px;
    color: var(--text-light);
    line-height: 1.75;
  }
  .contact-icon {
    width: 15px;
    height: 15px;
    flex: none;
  }
</style>
</head>
<body>
<main class="sheet">
  <section class="card card-back" aria-label="Card back">
    <span class="emboss-dot"></span>
    <span class="emboss-name">morventary</span>
  </section>

  <section class="card card-front" aria-label="Card front">
    <div class="brand">
      <span class="brand-dot"></span>
      <span class="brand-name">morventary</span>
    </div>
    <span class="divider"></span>
    <div class="contact-block">
      <h1 class="person-name">Karl Whitby</h1>
      <p class="person-title">Founder / CEO</p>
      <ul class="contact-list">
        <li class="contact-item">
          <svg class="contact-icon" viewBox="0 0 16 16" aria-hidden="true"><path fill="#29aee6" d="M3.6 1.2l2.3 2.6-1.3 1.8c.8 1.8 2.2 3.2 4 4l1.8-1.3 2.6 2.3-1.4 2.2C6.8 12.5 3.5 9.2 1.4 4.4z"/></svg>
          (999) 482-7160
        </li>
        <li class="contact-item">
          <svg class="contact-icon" viewBox="0 0 16 16" aria-hidden="true"><rect x="1" y="3" width="14" height="10" rx="1" fill="#29aee6"/><path d="M1.5 3.8L8 9l6.5-5.2" stroke="#232323" stroke-width="1.3" fill="none"/></svg>
          info@morventary.ai
        </li>
        <li class="contact-item">
          <svg class="contact-icon" viewBox="0 0 16 16" aria-hidden="true"><g fill="none" stroke="#29aee6" stroke-width="1.3"><circle cx="8" cy="8" r="6.5"/><ellipse cx="8" cy="8" rx="2.8" ry="6.5"/><path d="M1.5 8h13M2.6 4.5h10.8M2.6 11.5h10.8"/></g></svg>
          www.morventary.ai
        </li>
      </ul>
    </div>
  </section>
</main>
</body>
</html>
```